12 Kettles/12 Rivers Contest

The same as the previous project. This time, I need a flyer (A4 size) with the same design and use of logos. For the text, this is design #2.

Thank you.

I change to payment committed status. So I hope more designers will participate. Thank you.

For submissions, please only use the Russian text. The English text is for reference only. The flyer must be in Russian, expected for the title "12 Kettles/12 Rivers" which can be in English. Than you.

```html
<!DOCTYPE html>
<html lang="ru">
<head>
<meta charset="utf-8">
<title>12 Kettles/12 Rivers — конкурс</title>
<link href="https://fonts.googleapis.com/css2?family=Open+Sans:wght@400;600;700;800&family=Pangolin&display=swap" rel="stylesheet">
<style>
:root{
  --stage:#2b2b2d;
  --paper:#ffffff;
  --red:#d31f2f;
  --red-dark:#a8121f;
  --blue:#3a4aa0;
  --blue-dark:#1f2a6e;
  --sky:#1e8fdc;
  --ink:#1d2a66;
  --panel:#1c2240;
  --white:#ffffff;
}
*{box-sizing:border-box;margin:0;padding:0}
html,body{width:1200px;height:806px;overflow:hidden;background:var(--stage)}
body{position:relative;font-family:"Open Sans",Arial,sans-serif}
.flyer{position:absolute;top:38px;width:500px;height:730px;background:var(--paper);overflow:hidden;box-shadow:0 8px 24px rgba(0,0,0,.5)}
.flyer--front{left:62px}
.flyer--back{left:638px}
.header{position:absolute;left:0;top:0;width:100%;height:125px;background:var(--paper);z-index:2}
.seal{position:absolute;left:22px;top:22px;width:90px;height:90px;border-radius:50%;background:#e9dfb8;border:4px solid #c9a94a}
.brand{position:absolute;top:56px;display:flex;align-items:center;gap:8px;font-weight:800;color:var(--blue-dark);font-size:26px;letter-spacing:3px}
.brand--air{left:140px}
.brand__mark{width:22px;height:22px;border-radius:50%;background:var(--red)}
.brand--trade{left:370px;top:46px;flex-direction:column;align-items:flex-start;gap:4px;font-size:15px;letter-spacing:0;line-height:1.05}
.brand--trade .brand__mark{border-radius:0;width:36px;height:28px;background:var(--blue)}
.flag{position:absolute;left:0;top:125px;width:100%;height:605px;
  background:linear-gradient(168deg,#22317f 0%,#3c4ea6 24%,#e9ecf4 38%,#fbfbfb 44%,#d8212f 54%,#b8142a 62%,#f4f4f4 72%,#e2e2e2 76%,#d01d2d 86%,#a5111f 100%)}
.title{position:absolute;left:35px;top:165px;z-index:3;width:410px;height:125px}
.title__part{position:absolute;display:flex;flex-direction:column;align-items:center;justify-content:center;color:var(--white);font-weight:800;line-height:.95;text-align:center}
.title__part--left{left:0;top:0;background:var(--red);width:200px;height:117px;font-size:36px;padding-right:12px}
.title__part--right{left:210px;top:25px;background:var(--blue);width:200px;height:92px;font-size:36px;padding-left:10px}
.title__num{font-size:58px}
.title__slash{position:absolute;left:202px;top:-4px;width:5px;height:130px;background:var(--white);transform:skewX(-20deg)}
.ribbon{position:absolute;top:335px;height:120px;width:130px;z-index:3;border-radius:8px;background:linear-gradient(180deg,#e07f86,#8c95c8)}
.ribbon--left{left:12px}
.ribbon--right{right:12px}
.plate{position:absolute;left:130px;top:300px;width:240px;height:240px;border-radius:50%;z-index:4;
  background:radial-gradient(circle at 50% 45%,#ffffff 0%,#f1f1ee 60%,#d8d6cf 78%,#c4b98e 80%,#ecebe6 84%)}
.plate__text{position:absolute;left:130px;top:330px;width:240px;z-index:5;text-align:center}
.plate__label{display:inline-block;background:var(--red);color:var(--white);font-weight:800;font-size:22px;padding:2px 18px;margin-bottom:6px}
.plate__name{font-family:"Pangolin",cursive;color:var(--blue-dark);font-size:34px;line-height:1.05}
.cta{position:absolute;left:0;width:100%;z-index:3;text-align:center;color:var(--white)}
.cta__head{font-weight:800;font-size:30px;line-height:1.15;text-shadow:0 2px 4px rgba(0,0,0,.35)}
.cta__hint{font-size:13px;margin-top:6px}
.cta__link{display:inline-block;margin-top:6px;width:325px;padding:5px 0;border-radius:4px;background:linear-gradient(180deg,#4857ad,#2a3880);font-size:14px;font-weight:600;box-shadow:0 2px 4px rgba(0,0,0,.4)}
.flyer--front .cta{top:572px}
.flyer--back .cta{top:555px}
.promo{position:absolute;right:0;top:162px;width:300px;z-index:3;background:var(--red);color:var(--white);font-weight:800;font-size:13px;line-height:1.25;padding:8px 14px;text-align:center}
.rules-head{position:absolute;left:0;top:225px;width:100%;height:68px;z-index:3;background:linear-gradient(180deg,#2ea0ea,var(--sky) 60%,#1570b8);color:var(--white);font-weight:800;font-size:16px;line-height:1.3;padding:10px 20px}
.rules{position:absolute;left:0;top:293px;width:100%;height:230px;z-index:3;background:linear-gradient(90deg,var(--panel),#3c4466 70%,#8a8fa3)}
.steps{list-style:none;position:absolute;left:22px;top:16px;width:222px;color:var(--white);font-weight:700;font-size:11px;line-height:1.3}
.steps li{margin-bottom:9px;display:flex;gap:6px}
.steps__num{font-size:17px;line-height:1}
.screen{position:absolute;left:250px;top:10px;width:240px;height:190px;border-radius:4px;background:linear-gradient(160deg,#e8ecf4,#c7cfe0 55%,#9aa4bd)}
</style>
</head>
<body>

<section class="flyer flyer--front">
  <header class="header">
    <div class="seal" role="img" aria-label="Круглая печать партнёра"></div>
    <div class="brand brand--air"><span class="brand__mark"></span>AEROVIA</div>
    <div class="brand brand--trade"><span class="brand__mark"></span>Trade<br>Bureau</div>
  </header>
  <div class="flag" role="img" aria-label="Развевающийся флаг США"></div>
  <div class="title">
    <div class="title__part title__part--left"><span class="title__num">12</span>Kettles</div>
    <div class="title__part title__part--right"><span class="title__num">12</span>Rivers</div>
    <span class="title__slash"></span>
  </div>
  <div class="ribbon ribbon--left" role="img" aria-label="Декоративная лента в цветах флага"></div>
  <div class="ribbon ribbon--right" role="img" aria-label="Декоративная лента в цветах флага"></div>
  <div class="plate" role="img" aria-label="Белая фарфоровая тарелка"></div>
  <div class="plate__text">
    <span class="plate__label">КОНКУРС</span>
    <p class="plate__name">"Кулинарный<br>туризм<br>США"</p>
  </div>
  <div class="cta">
    <p class="cta__head">ВЫИГРАЙТЕ БЕСПЛАТНУЮ<br>ПОЕЗДКУ В США!</p>
    <p class="cta__hint">кликните здесь, чтобы узнать больше</p>
    <span class="cta__link">http://12kettles-rivers.bloghub.net</span>
  </div>
</section>

<section class="flyer flyer--back">
  <header class="header">
    <div class="seal" role="img" aria-label="Круглая печать партнёра"></div>
    <div class="brand brand--air"><span class="brand__mark"></span>AEROVIA</div>
    <div class="brand brand--trade"><span class="brand__mark"></span>Trade<br>Bureau</div>
  </header>
  <div class="flag" role="img" aria-label="Развевающийся флаг США"></div>
  <p class="promo">МАРКЕТИНГОВАЯ КАМПАНИЯ ПО ПРОДВИЖЕНИЮ КУЛИНАРНЫХ ТУРОВ И ТУРИЗМА В США</p>
  <p class="rules-head">ДЛЯ ТОГО, ЧТОБЫ ВЫИГРАТЬ БЕСПЛАТНУЮ ПОЕЗДКУ В США НЕОБХОДИМО:</p>
  <div class="rules">
    <ol class="steps">
      <li><span class="steps__num">1.</span><span>ЗАЛАЙКАТЬ И ПОДЕЛИТЬСЯ НАШЕЙ СТРАНИЧКОЙ В ФРЕНДЛАЙНЕ</span></li>
      <li><span class="steps__num">2.</span><span>ЕЖЕДНЕВНО ПРОВЕРЯТЬ ПОСТЫ НА НАШЕЙ СТРАНИЦЕ В ФРЕНДЛАЙНЕ</span></li>
      <li><span class="steps__num">3.</span><span>УЧАСТВОВАТЬ: РАССКАЗАТЬ В СВОИХ ПОСТАХ КАКИЕ БЛЮДА АМЕРИКАНСКОЙ КУХНИ И ГДЕ ВЫ БЫ СЬЕЛИ</span></li>
      <li><span class="steps__num">4.</span><span>РЕГУЛЯРНО ГОЛОСОВАТЬ ЗА ПОСТЫ НА НАШЕЙ СТРАНИЦЕ</span></li>
    </ol>
    <div class="screen" role="img" aria-label="Снимок страницы конкурса в социальной сети"></div>
  </div>
  <div class="cta">
    <p class="cta__head">ВЫИГРАЙТЕ БЕСПЛАТНУЮ<br>ПОЕЗДКУ В США!</p>
    <p class="cta__hint">кликните здесь, чтобы узнать больше</p>
    <span class="cta__link">http://12kettles-rivers.bloghub.net</span>
  </div>
</section>

</body>
</html>
```